Mexican construction company needs a business card design

We need a business card design for a company based in Monterrey, Mexico called:

Desarrollos Tolvani S.A. de C.V.

The company is in the construction business and I would like the businees card to be simple and concise. Please use white background and blue or black text color that say:

"Proyectos de Construcción"-- (Brief description of business)
" Rodrigo Ulloa Benítez"--- (My name)
"rulloab@correovelo.mx"-- (My email)
"C: (81) 82 19 57 46"-- (My cell)
"O: (81) 86 72 13 95"-- (Office phone)

Please use only the colors of my company that are attached

Please make the back of the business card blue (same blue from logo) and use the logo.

Thanks!

```html
<!DOCTYPE html>
<html lang="es">
<head>
<meta charset="utf-8">
<title>Desarrollos Tolvani – Tarjeta de presentación</title>
<link rel="stylesheet" href="https://fonts.googleapis.com/css2?family=Nunito+Sans:wght@300;400;800&display=swap">
<style>
  :root {
    --navy: #1f1f52;
    --grey: #a4a4a4;
    --rule: #8a8a8a;
    --ink: #3c3c3c;
    --card: #ffffff;
    --backdrop: #eceef0;
  }
  * { margin: 0; padding: 0; box-sizing: border-box; }
  html, body { width: 1200px; height: 800px; overflow: hidden; }
  body {
    background: var(--backdrop);
    font-family: "Nunito Sans", Arial, sans-serif;
    position: relative;
  }
  .card {
    position: absolute;
    top: 248px;
    width: 520px;
    height: 300px;
    background: var(--card);
    box-shadow: 0 2px 10px rgba(0,0,0,0.08);
  }
  .card--brand { left: 60px; }
  .card--contact { left: 620px; }

  .bar {
    position: absolute;
    height: 9px;
    background: var(--navy);
  }
  .card--brand .bar--top { top: 26px; left: 26px; right: 60px; }
  .card--brand .bar--bottom { bottom: 26px; left: 180px; right: 60px; }

  .brand {
    position: absolute;
    left: 70px;
    top: 104px;
    display: flex;
    align-items: center;
    gap: 22px;
  }
  .brand__square {
    width: 84px;
    height: 84px;
    background: var(--grey);
  }
  .brand__name {
    color: var(--navy);
    font-weight: 800;
    text-transform: uppercase;
    line-height: 1;
  }
  .brand__line1 { display: block; font-size: 27px; letter-spacing: 2px; }
  .brand__line2 { display: block; font-size: 50px; letter-spacing: 3px; margin-top: 2px; }

  .card--contact .bar--top { top: 24px; left: 22px; right: 30px; }
  .card--contact .bar--bottom { bottom: 34px; left: 160px; right: 12px; }

  .nameplate {
    position: absolute;
    top: 48px;
    left: 262px;
    width: 236px;
    height: 78px;
    background: var(--grey);
    color: #fff;
    padding: 12px 14px;
  }
  .nameplate__name { font-weight: 300; font-size: 20px; letter-spacing: 0.3px; }
  .nameplate__role { font-weight: 300; font-size: 12.5px; margin-top: 4px; }

  .contact-list {
    position: absolute;
    top: 138px;
    left: 80px;
    width: 196px;
    list-style: none;
    border-top: 1px solid var(--rule);
  }
  .contact-list li {
    height: 28px;
    border-bottom: 1px solid var(--rule);
    display: flex;
    align-items: flex-end;
    justify-content: flex-end;
    padding: 0 2px 4px;
    font-size: 11px;
    color: var(--ink);
    letter-spacing: 0.4px;
  }
</style>
</head>
<body>
  <section class="card card--brand" aria-label="Reverso de la tarjeta">
    <div class="bar bar--top"></div>
    <div class="brand">
      <div class="brand__square"></div>
      <div class="brand__name">
        <span class="brand__line1">Desarrollos</span>
        <span class="brand__line2">Tolvani</span>
      </div>
    </div>
    <div class="bar bar--bottom"></div>
  </section>

  <section class="card card--contact" aria-label="Frente de la tarjeta">
    <div class="bar bar--top"></div>
    <div class="nameplate">
      <p class="nameplate__name">Rodrigo Ulloa Benítez</p>
      <p class="nameplate__role">Proyectos de Construcción</p>
    </div>
    <ul class="contact-list">
      <li>C. (81) 82 19 57 46</li>
      <li>O. (81) 86 72 13 95</li>
      <li>rulloab@correovelo.mx</li>
      <li></li>
    </ul>
    <div class="bar bar--bottom"></div>
  </section>
</body>
</html>
```